Eye catching while remaining subtle, stylish and professional

Pellmore Works are a Heatpump and Air Conditioning Company. I would like stationary that would be suitable to use for letters, quoting invoicing. The final design should communicate a trade/service type industry that is clean and professional

I would like the designer to also offer a Business card option as well.

Details should include company logo as attached. Company details. Name, Address, Phone, Email and Website. You can use generic details until a final design is chosen

Target Market(s)

Trade/Service Industry

Industry/Entity Type

Air Conditioning

Requirements
Must have
• LOGO, Company contact details
Nice to have
• Watermark

```html
<!DOCTYPE html>
<html lang="en">
<head>
<meta charset="utf-8">
<title>Pellmore Works – Business Card</title>
<link href="https://fonts.googleapis.com/css2?family=Questrial&display=swap" rel="stylesheet">
<style>
  :root {
    --bg: #e3e5e7;
    --blue-deep: #0b7cb8;
    --blue-mid: #3a97c6;
    --blue-pale: #93b9cf;
    --card-white: #fbfbfb;
    --band-grey: #dcdcdc;
    --ink: #3c3c3c;
    --accent: #1a92d6;
    --logo-light: #e9ecee;
  }
  * { box-sizing: border-box; margin: 0; padding: 0; }
  html, body { width: 1200px; height: 1000px; overflow: hidden; }
  body {
    background: var(--bg);
    font-family: "Questrial", "Century Gothic", sans-serif;
    display: flex;
    align-items: center;
    justify-content: center;
    gap: 40px;
  }
  .card {
    width: 525px;
    height: 300px;
    position: relative;
    box-shadow: 0 6px 18px rgba(0,0,0,0.12);
    overflow: hidden;
  }
  .card--front {
    background: linear-gradient(90deg, var(--blue-deep) 0%, var(--blue-mid) 50%, var(--blue-pale) 100%);
    display: flex;
    align-items: center;
    justify-content: center;
  }
  .card--front .brand-name {
    color: var(--logo-light);
    font-size: 44px;
    letter-spacing: 3px;
    text-transform: uppercase;
  }
  .card--back { background: var(--card-white); }
  .card--back .brand-name {
    position: absolute;
    left: 34px;
    top: 60px;
    color: var(--accent);
    font-size: 32px;
    letter-spacing: 2px;
    text-transform: uppercase;
  }
  .contact {
    position: absolute;
    left: 292px;
    top: 104px;
    color: var(--ink);
    font-size: 13px;
    line-height: 17px;
  }
  .contact__name {
    color: var(--accent);
    font-size: 15px;
    letter-spacing: 1px;
    text-transform: uppercase;
    font-weight: 700;
  }
  .contact__role { margin-bottom: 4px; }
  .contact__line { display: flex; align-items: center; gap: 6px; }
  .contact__icon { width: 13px; height: 13px; flex: none; }
  .contact__address { margin-top: 6px; }
  .pattern-band {
    position: absolute;
    left: 0; right: 0; bottom: 0;
    height: 58px;
    background: var(--band-grey);
  }
</style>
</head>
<body>
  <section class="card card--front">
    <span class="brand-name">Pellmore Works</span>
  </section>

  <section class="card card--back">
    <span class="brand-name">Pellmore Works</span>

    <div class="contact">
      <p class="contact__name">Sam Thornley</p>
      <p class="contact__role">General Manager</p>
      <p class="contact__line">
        <svg class="contact__icon" viewBox="0 0 13 13"><rect width="13" height="13" rx="2" fill="#1a92d6"/><path d="M4 3 l1.5 0 l.6 2 l-1 .8 q.9 1.8 2.5 2.5 l.8-1 l2 .6 v1.5 q-4.5.4-6.4-6.4z" fill="#fff"/></svg>
        009 41 73 00 18
      </p>
      <p class="contact__line">
        <svg class="contact__icon" viewBox="0 0 13 13"><rect width="13" height="13" rx="2" fill="#1a92d6"/><rect x="3" y="4" width="7" height="5" fill="none" stroke="#fff" stroke-width="1"/><path d="M3 4 l3.5 3 l3.5-3" fill="none" stroke="#fff" stroke-width="1"/></svg>
        info@pellmoreworks.com
      </p>
      <p class="contact__line">
        <svg class="contact__icon" viewBox="0 0 13 13"><rect width="13" height="13" rx="2" fill="#1a92d6"/><circle cx="6.5" cy="6.5" r="3.5" fill="none" stroke="#fff" stroke-width="1"/><path d="M3 6.5 h7 M6.5 3 v7" stroke="#fff" stroke-width="0.8"/></svg>
        www.pellmoreworks.com
      </p>
      <p class="contact__address">7/12 Harlow Street<br>Kingsbury, VIC 3072</p>
    </div>

    <div class="pattern-band" role="img" aria-label="Band of light grey repeating snowflake-arrow pattern along the card edge"></div>
  </section>
</body>
</html>
```